Redesign of Grantlyhub.com

We need a redesign of some key-pages on our crowdfunding website for mobile apps, GrantlyHub.com.

- Redesign of homepage
http://www.grantlyhub.com/en

- Redesign of project submission page
http://www.grantlyhub.com/en/submit-your-app/submit-your-app

- Redesign of browsing section
http://www.grantlyhub.com/en/fund-apps

- Redesign of project funding page
http://www.grantlyhub.com/en/fund-apps/sponsor/sketch-riddler?amount=5.00

Design should be highly focused on a great user experience for users of the platform, being in principal mobile developers. So we need a great user experience for mobile developers using our service.

Benchmark designs we particularly like are:
http://www.pledgorama.com/
http://www.tradebitly.com/landing/
http://www.vomba.com/

Design should have a more 'fun, happy to get involved' factor as it has nox.
Updates

Logo's have been uploaded

Target Market(s)

mobile app developers

Industry/Entity Type

Crowdfunding

Requirements
Must have
• Submission forms must have explanation fields next to the form

Homepage should have design in whihc a introductary video can be integrated

```html
<!DOCTYPE html>
<html lang="en">
<head>
<meta charset="utf-8">
<title>GrantlyHub – Crowdfunding mobile apps</title>
<link href="https://fonts.googleapis.com/css2?family=Arimo:wght@400;700&family=Cabin:wght@400;500&family=Ubuntu:wght@700&display=swap" rel="stylesheet">
<style>
:root{
  --lime:#9bc70f;
  --lime-dark:#6f9a07;
  --lime-light:#c9e22a;
  --text-green:#7ba50a;
  --blue:#1b6fb5;
  --blue-dark:#0f4f8c;
  --navy:#1c3d6b;
  --ink:#333;
  --muted:#555;
  --grey-bg:#eef0f2;
  --white:#fff;
}
*{box-sizing:border-box;margin:0;padding:0}
html,body{width:986px;height:1200px;overflow:hidden}
body{position:relative;background:var(--white);font-family:"Cabin",sans-serif;color:var(--ink)}
.abs{position:absolute}

/* top bar */
.topbar{left:0;top:0;width:986px;height:33px;background:linear-gradient(#9bc615,#86b00a)}
.topbar nav{position:absolute;left:395px;top:0;height:33px;display:flex;align-items:center;gap:0;font:700 8.5px "Arimo",sans-serif;color:#fff}
.topbar nav span{padding:0 11px;border-right:1px solid rgba(0,0,0,.12);line-height:33px}
.topbar .new{background:var(--blue);border-radius:6px;padding:1px 4px;font-size:7px;margin-right:4px}
.topbar .account{position:absolute;left:650px;top:0;width:124px;height:33px;background:rgba(0,0,0,.08);display:flex;align-items:center;justify-content:space-around;font:700 8.5px "Arimo",sans-serif;color:#fff}
.search{left:775px;top:6px;width:86px;height:20px;background:#fff;font:italic 8px "Arimo",sans-serif;color:#aaa;padding:5px 6px}
.search-icon{left:870px;top:10px}

/* header */
.header{left:0;top:33px;width:986px;height:62px;background:#fff}
.brand{left:106px;top:40px;display:flex;align-items:center;gap:7px}
.brand .mark{width:26px;height:26px;background:var(--blue)}
.brand .name{font:500 22px "Cabin",sans-serif;color:var(--blue)}
.mainnav{left:244px;top:33px;height:62px;display:flex;align-items:center;font:700 9.5px "Arimo",sans-serif;color:#333}
.mainnav a{text-decoration:none;color:inherit;margin-right:31px}
.mainnav .home{color:var(--blue);margin-right:31px}

/* hero */
.hero{left:0;top:95px;width:986px;height:248px;background:linear-gradient(160deg,#8fbc10 0%,#a9cf14 45%,#d6e81e 100%)}
.hero h1{position:absolute;left:104px;top:18px;font:700 31px "Ubuntu",sans-serif;color:#fff;text-shadow:0 2px 3px rgba(0,0,0,.25)}
.bubble{top:178px;width:212px;height:121px;background:#2a2a2a;border-radius:7px;padding:6px}
.bubble .inner{background:linear-gradient(#fff,#e9e9e9);border-radius:4px;height:100%;padding:8px 9px}
.bubble h2{font:400 15px "Cabin",sans-serif;color:var(--blue);text-align:center;margin-bottom:7px}
.bubble li{list-style:none;font-size:10px;color:#444;display:flex;align-items:center;gap:6px;height:21px}
.tick{width:14px;height:14px;border-radius:50%;background:var(--blue);flex:none}
.bubble .tail{position:absolute;left:99px;bottom:-10px;border:8px solid transparent;border-top-color:#2a2a2a;border-bottom:0}
.rail{left:0;top:343px;width:630px;height:9px;background:linear-gradient(#b8d81a,#7ea90a)}
.knob{width:41px;height:41px;border-radius:50%;background:radial-gradient(circle at 40% 35%,#a6d11b,#5d8d05);top:328px}
.knob::after{content:"";position:absolute;left:14px;bottom:-18px;border:6px solid transparent;border-bottom-color:var(--blue)}
.knob.fund::after{border-bottom-color:var(--lime)}
.cta{top:387px;width:166px;height:29px;border-radius:15px;font:700 13px "Arimo",sans-serif;color:#fff;display:flex;align-items:center;justify-content:center;box-shadow:0 2px 3px rgba(0,0,0,.2)}
.cta.start{left:124px;background:linear-gradient(#2a86cf,var(--blue-dark))}
.cta.funding{left:353px;background:linear-gradient(#b9d935,#8fb80f)}
.phones{left:630px;top:124px;width:257px;height:242px;border-radius:14px;background:linear-gradient(90deg,#222 0 49%,transparent 49% 51%,#222 51%)}
.phones .screen1{position:absolute;left:10px;top:28px;width:108px;height:181px;background:linear-gradient(135deg,#1a7cd0,#0d5aa8)}
.phones .screen2{position:absolute;left:143px;top:44px;width:104px;height:150px;background:linear-gradient(135deg,#1a7cd0,#0d5aa8)}
.social{left:684px;top:394px;display:flex;align-items:center;gap:8px;font-size:12px;color:#444}
.social .net{display:flex;align-items:center;gap:4px;color:var(--blue-dark);font-size:11px}
.social .dot{width:14px;height:14px;border-radius:50%;background:var(--blue-dark)}

/* video band */
.band{left:0;top:448px;width:986px;height:330px;background:var(--grey-bg)}
.section-title{font:400 22px "Cabin",sans-serif;color:#444}
.video{left:99px;top:509px;width:516px;height:248px;background:linear-gradient(135deg,#156bb3,#2b8fd8)}
.video .play{position:absolute;left:205px;top:68px;width:108px;height:108px;border-radius:12px;background:rgba(255,255,255,.55)}
.video .play::after{content:"";position:absolute;left:41px;top:31px;border-left:36px solid #111;border-top:23px solid transparent;border-bottom:23px solid transparent}
.video p{position:absolute;left:0;width:100%;top:194px;text-align:center;color:#fff;font:400 23px "Cabin",sans-serif}
.tabs{left:641px;top:509px;width:246px;height:34px;border-bottom:1px solid #ccc;display:flex;font-size:12px}
.tabs span{width:121px;display:flex;align-items:center;justify-content:center;color:#777}
.tabs .on{background:#fff;border:1px solid #ccc;border-bottom:0;color:var(--blue)}
.steps{left:641px;top:553px;width:260px;list-style:none;font:400 15px/1.3 "Cabin",sans-serif;color:var(--text-green)}
.steps li{margin-bottom:9px}
.more{left:640px;top:728px;width:165px;height:29px;border-radius:15px;background:linear-gradient(#2a86cf,var(--blue-dark));color:#fff;font:700 13px "Arimo",sans-serif;display:flex;align-items:center;justify-content:center}

/* listings */
.group-title{display:flex;align-items:center;gap:9px;font:400 22px "Cabin",sans-serif;color:#444}
.icon-badge{width:26px;height:26px}
.row{display:flex}
.item{width:78px;display:flex;flex-direction:column;align-items:center;font-size:10.5px;color:#444}
.thumb{width:53px;height:53px;border-radius:3px;margin-bottom:10px}
.divider{left:99px;width:790px;height:1px;background:#e4e4e4}

/* footer */
.footer{left:0;top:1110px;width:986px;height:90px;background:var(--grey-bg)}
.footer h3{font:400 10px "Cabin",sans-serif;color:#444;position:absolute;top:21px}
.logos{position:absolute;top:43px;display:flex;align-items:center;gap:14px;font:500 12px "Cabin",sans-serif;color:#333}
.logos .sq{display:inline-block;width:9px;height:9px;background:#888;margin-right:4px;vertical-align:middle}
</style>
</head>
<body>

<div class="abs topbar">
  <nav>
    <span><b class="new">NEW</b>BLOG</span>
    <span>GET AAA CERTIFIED</span>
    <span>ABOUT US</span>
  </nav>
  <div class="account"><span>LOG IN</span><span>SIGN UP</span></div>
</div>
<div class="abs search">Search...</div>
<svg class="abs search-icon" width="11" height="11" viewBox="0 0 11 11"><circle cx="4.5" cy="4.5" r="3.3" fill="none" stroke="#fff" stroke-width="1.6"/><path d="M7 7l3 3" stroke="#fff" stroke-width="1.8"/></svg>

<header class="abs header"></header>
<div class="abs brand"><span class="mark"></span><span class="name">GrantlyHub</span></div>
<nav class="abs mainnav">
  <a class="home" href="#">&#8962; HOME</a>
  <a href="#">FUND APPS</a>
  <a href="#">SUBMIT YOUR APP</a>
  <a href="#">FIND A DEVELOPER</a>
  <a href="#">HOW IT WORKS</a>
  <a href="#">REGISTER</a>
</nav>

<section class="abs hero"><h1>Crowdfunding mobile apps</h1></section>

<div class="abs bubble" style="left:105px">
  <div class="inner">
    <h2>App builders</h2>
    <ul><li><i class="tick"></i>Fund your development</li><li><i class="tick"></i>Get downloads</li><li><i class="tick"></i>Keep 100% ownership</li></ul>
  </div><span class="tail"></span>
</div>
<div class="abs bubble" style="left:332px">
  <div class="inner">
    <h2>Funders</h2>
    <ul><li><i class="tick"></i>Get great returns on your funding</li><li><i class="tick"></i>Fund per milestone</li><li><i class="tick"></i>Be part of a succes story</li></ul>
  </div><span class="tail"></span>
</div>

<div class="abs rail"></div>
<div class="abs knob" style="left:186px"></div>
<div class="abs knob fund" style="left:415px"></div>
<a class="abs cta start">START PROJECT</a>
<a class="abs cta funding">START FUNDING</a>

<div class="abs phones" role="img" aria-label="Two smartphones showing a rising funding graph with a dollar coin">
  <div class="screen1"></div><div class="screen2"></div>
</div>

<div class="abs social">Find us on social media:
  <span class="net"><i class="dot"></i>Friendnet</span>
  <span class="net"><i class="dot"></i>Chirper</span>
</div>

<section class="abs band"></section>
<h2 class="abs section-title" style="left:99px;top:466px">Watch the video</h2>
<div class="abs video"><span class="play"></span><p>How GrantlyHub works</p></div>

<h2 class="abs section-title" style="left:640px;top:466px">How it works</h2>
<div class="abs tabs"><span class="on">Developers</span><span>Funders</span></div>
<ol class="abs steps">
  <li>Tell us the story behind your app.</li>
  <li>Start receiving pledges.</li>
  <li>Promote and build-up funders.</li>
  <li>Get 80% of the funds per milestone.</li>
  <li>Publish your app on the AppVault or Droidmarket</li>
</ol>
<a class="abs more">FIND OUT MORE</a>

<!-- Most funded -->
<div class="abs group-title" style="left:99px;top:800px">
  <svg class="icon-badge" viewBox="0 0 26 26"><circle cx="13" cy="11" r="9" fill="var(--lime)"/><path d="M8 18l-2 7 7-3 7 3-2-7" fill="var(--lime-dark)"/></svg>Most funded
</div>
<div class="abs row" style="left:94px;top:852px">
  <div class="item"><span class="thumb" role="img" aria-label="App icon: chalkboard game" style="background:#3b3a36"></span>Sketch riddl...</div>
  <div class="item"><span class="thumb" role="img" aria-label="App icon: pattern game" style="background:#c8281e"></span>PatternPika</div>
  <div class="item"><span class="thumb" role="img" aria-label="App icon: orange letter tile" style="background:#555"></span>Hoolumi</div>
</div>

<div class="abs group-title" style="left:368px;top:800px">
  <svg class="icon-badge" viewBox="0 0 26 26"><path d="M13 24L3 13a6 6 0 0110-7 6 6 0 0110 7z" fill="var(--lime-light)"/></svg>Our picks
</div>
<div class="abs row" style="left:363px;top:852px">
  <div class="item"><span class="thumb" role="img" aria-label="App icon: cartoon game" style="background:#d98a20"></span>Pongo Master</div>
  <div class="item"><span class="thumb" role="img" aria-label="App icon: quiz scoreboard" style="background:#6e5a48"></span>Gold Rush quiz</div>
  <div class="item"><span class="thumb" role="img" aria-label="App icon: coupon cube" style="background:#e94f8c"></span>Mysavers</div>
</div>

<div class="abs group-title" style="left:640px;top:800px">
  <svg class="icon-badge" viewBox="0 0 26 26"><circle cx="13" cy="8" r="6" fill="var(--lime)"/><path d="M2 25c0-8 5-11 11-11s11 3 11 11z" fill="var(--lime)"/></svg>Most Active Funders
</div>
<div class="abs row" style="left:632px;top:852px">
  <div class="item"><span class="thumb" role="img" aria-label="Funder profile photo" style="background:#888"></span>Lucien</div>
  <div class="item"><span class="thumb" role="img" aria-label="Funder avatar illustration" style="background:#dfe4f2"></span>Marten</div>
  <div class="item"><span class="thumb" role="img" aria-label="Funder profile photo" style="background:#b7826a"></span>Jorin</div>
</div>

<div class="abs divider" style="top:945px"></div>

<div class="abs group-title" style="left:99px;top:964px">
  <svg class="icon-badge" viewBox="0 0 26 26"><path d="M2 14l8 7L24 5" fill="none" stroke="var(--lime)" stroke-width="4"/></svg>Funded
</div>
<div class="abs row" style="left:94px;top:1013px">
  <div class="item"><span class="thumb" role="img" aria-label="App icon: phone with certification badge" style="background:#c33b30"></span>Sketch riddl...</div>
  <div class="item"><span class="thumb" role="img" aria-label="App icon: printer" style="background:#c9c9c9"></span>AppQ</div>
  <div class="item"><span class="thumb" role="img" aria-label="App icon: orange letter tile" style="background:#555"></span>Huolumi</div>
  <div class="item"><span class="thumb" role="img" aria-label="App icon: cartoon game with certification badge" style="background:#d98a20"></span>RadioNO</div>
  <div class="item"><span class="thumb" role="img" aria-label="App icon: coupon cube" style="background:#e94f8c"></span>DealCube</div>
  <div class="item"><span class="thumb" role="img" aria-label="App icon: quiz scoreboard" style="background:#6e5a48"></span>Gold Rush</div>
  <div class="item"><span class="thumb" role="img" aria-label="App icon: pattern game" style="background:#c8281e"></span>Pan Po</div>
</div>

<div class="abs group-title" style="left:640px;top:964px">
  <svg class="icon-badge" viewBox="0 0 26 26"><path d="M10 3h6v7h7v6h-7v7h-6v-7H3v-6h7z" fill="var(--lime)"/></svg>New members
</div>
<div class="abs row" style="left:632px;top:1013px">
  <div class="item"><span class="thumb" role="img" aria-label="Member avatar: gear emblem" style="background:#3a3a3a;border-radius:50%"></span>Aldo</div>
  <div class="item"><span class="thumb" role="img" aria-label="Member profile photo outdoors" style="background:#6d7a52"></span>Teo</div>
  <div class="item"><span class="thumb" role="img" aria-label="Default member silhouette" style="background:#cfd6e8"></span>Gita</div>
</div>

<footer class="abs footer">
  <h3 style="left:103px">Our partners</h3>
  <div class="logos" style="left:103px">
    <span><i class="sq"></i>Nexora</span><span>Mobile Norse</span><span>NTQ</span><span>jade lodestar</span><span>ikkt</span>
  </div>
  <h3 style="left:541px">Featured on</h3>
  <div class="logos" style="left:541px;gap:10px;font-size:10px">
    <span>The Capital Ledger</span><span>VenturePulse</span><span>ZQNet</span><span>StackBase</span><span>bytenews</span>
  </div>
</footer>

</body>
</html>
```